TRAVIM 2026 Flyer for Conference

TRAVIM needs a design for a 1-page flyer that we will hand out at an upcoming event & then later post online as a pdf. There are 3 elements which need to be on the flyer:

1) A logo. This should be prominent on the design (e.g., in the middle). The flyer should use the colors that are in that logo (e.g., for accents, design elements, and/or text; not all of these have to be used):
Dark blue: #185577
Med blue: #327C9A
Teal: #4EB1C2
Light Teal: #9EDBE6

2) The conference theme -- Oceans of Knowledge: Diving into Information Literacy -- should be at the flyer's top.

3) Finally, these six tracks should be listed below the theme and the logo (it's font size should be at least a couple sizes smaller than the size used for the theme):
- Pearls of Pedagogy: Teaching Techniques that Work
- The Depth Gauge: Measuring Instructional Impact
- Techtonic Shifts: Innovation and Educational Technology
- Captain's Log: Navigating Leadership in Library Instruction
- Swimming Together: Collaborating with Others
- The Bermuda Triangle: Exploring (Seemingly) Eternal Challenges

Font styles to use
Sans Serif

Colors
0094D4
00A9DD
6FCCEA
C7EBF8
E9F6FB

Requirements
Must have
• The 3 elements listed in the description: 1) the logo, 2) the text of the theme and 3) the text for the tracks.

```html
<!DOCTYPE html>
<html lang="en">
<head>
<meta charset="utf-8">
<title>TRAVIM 2026 — Oceans of Knowledge</title>
<link rel="stylesheet" href="https://fonts.googleapis.com/css2?family=Arimo:wght@700&family=Nunito+Sans:wght@800&family=Questrial&display=swap">
<style>
  :root {
    --stage: #333333;
    --paper: #ffffff;
    --dark-blue: #185577;
    --med-blue: #327C9A;
    --teal: #4EB1C2;
    --light-teal: #9EDBE6;
    --track-blue: #1f74b8;
    --body-ink: #2b2b2b;
  }
  * { box-sizing: border-box; margin: 0; padding: 0; }
  html, body { width: 1200px; height: 1200px; overflow: hidden; background: var(--stage); }
  .flyer {
    position: absolute; left: 196px; top: 30px;
    width: 808px; height: 1140px;
    background: var(--paper);
    overflow: hidden;
  }
  .brand {
    position: absolute; left: 75px; top: 120px;
    display: flex; align-items: center; gap: 14px;
  }
  .brand-dot { width: 34px; height: 34px; border-radius: 50%; background: var(--teal); }
  .brand-name {
    font-family: "Arimo", sans-serif; font-weight: 700;
    font-size: 56px; color: var(--dark-blue); letter-spacing: 1px;
  }
  .event-meta {
    position: absolute; left: 123px; top: 200px;
    font-family: "Nunito Sans", sans-serif; font-weight: 800;
    font-size: 15px; letter-spacing: 3px; color: var(--teal);
  }
  .theme { position: absolute; left: 75px; top: 322px; }
  .theme-title {
    font-family: "Arimo", sans-serif; font-weight: 700;
    font-size: 31px; color: var(--dark-blue); letter-spacing: 0.5px; line-height: 1.1;
  }
  .theme-subtitle {
    font-family: "Arimo", sans-serif; font-weight: 400;
    font-size: 21.5px; color: var(--teal); margin-top: 4px; letter-spacing: 0.2px;
  }
  .theme-rule { width: 233px; height: 2px; background: var(--dark-blue); margin-top: 10px; }
  .tracks { position: absolute; left: 76px; top: 418px; list-style: none; }
  .track { height: 38px; }
  .track-name {
    display: block; font-family: "Nunito Sans", sans-serif; font-weight: 800;
    font-size: 14.5px; color: var(--track-blue); line-height: 19px;
  }
  .track-desc {
    display: block; font-family: "Questrial", sans-serif;
    font-size: 15px; color: var(--body-ink); line-height: 19px;
  }
  .shore { position: absolute; left: 0; top: 0; width: 808px; height: 1140px; }
</style>
</head>
<body>
  <main class="flyer">
    <div class="brand">
      <span class="brand-dot"></span>
      <span class="brand-name">TRAVIM 2026</span>
    </div>
    <div class="event-meta">NORFOLK, VA · MAY 7-9</div>

    <header class="theme">
      <h1 class="theme-title">OCEANS OF KNOWLEDGE</h1>
      <h2 class="theme-subtitle">DIVING INTO INFORMATION LITERACY</h2>
      <div class="theme-rule"></div>
    </header>

    <ul class="tracks">
      <li class="track"><span class="track-name">Pearls of Pedagogy:</span><span class="track-desc">Teaching Techniques that Work</span></li>
      <li class="track"><span class="track-name">The Depth Gauge:</span><span class="track-desc">Measuring Instructional Impact</span></li>
      <li class="track"><span class="track-name">Techtonic Shifts:</span><span class="track-desc">Innovation and Educational Technology</span></li>
      <li class="track"><span class="track-name">Captain's Log:</span><span class="track-desc">Navigating Leadership in Library Instruction</span></li>
      <li class="track"><span class="track-name">Swimming Together:</span><span class="track-desc">Collaborating with Others</span></li>
      <li class="track"><span class="track-name">The Bermuda Triangle:</span><span class="track-desc">Exploring (Seemingly) Eternal Challenges</span></li>
    </ul>

    <svg class="shore" viewBox="0 0 808 1140" aria-hidden="false">
      <defs>
        <linearGradient id="sea" x1="0" y1="0" x2="0" y2="1" gradientUnits="objectBoundingBox">
          <stop offset="0" stop-color="#0f8f8c"/>
          <stop offset="0.55" stop-color="#17a59d"/>
          <stop offset="0.78" stop-color="#4fb3a6"/>
          <stop offset="0.86" stop-color="#c4a47c"/>
          <stop offset="0.93" stop-color="#e8ece8"/>
          <stop offset="1" stop-color="#e0a983"/>
        </linearGradient>
      </defs>
      <polygon role="img" aria-label="Aerial photo of turquoise sea meeting a sandy beach with white surf"
               points="808,310 808,1140 0,1140" fill="url(#sea)"/>
      <line x1="810" y1="308" x2="-2" y2="1142" stroke="var(--dark-blue)" stroke-width="4"/>
    </svg>
  </main>
</body>
</html>
```